BrevoLunt Business Card Design Project

We are looking for a modern, clean business card design for our new company. We are a consulting firm focused on the financial services market providing management and IT consulting to banks, insurance companies, etc. Please include our company logo and company contact information from the attached file in the design. Two versions of the logo are attached, either version is acceptable. Logos are available in other file formats if needed. We would like to include the contact information for both our UK and US offices as well as the following information for each individual card holder: Name, position/title, address, phone number and e-mail address.
Updates
Project Deadline Extended
Reason: A last minute trip over seas has prevented us from finalizing the decision. A decision will be made this week. We apologize for the inconvenience.
Industry/Entity Type
Business
Contact Information for Business Card
Company logo.
Company locations and phone numbers for both the US and UK offices.
Company URL.
Cardholder Name
Cardholder Position/title
Cardholder Address
Cardholder Phone Number
Cardholder e-mail Address
Look and feel
Each slider illustrates characteristics of the customer's brand and the style your logo design should communicate.

```html
<!DOCTYPE html>
<html lang="en">
<head>
<meta charset="utf-8">
<title>BrevoLunt Business Card</title>
<link rel="stylesheet" href="https://fonts.googleapis.com/css2?family=Open+Sans:wght@400;600;700&display=swap">
<style>
  :root {
    --navy: #14305e;
    --navy-deep: #0d2450;
    --navy-light: #1f3f74;
    --ink: #5a5a5a;
    --paper: #ffffff;
    --backdrop: #ecebe8;
    --rule: #2b2b2b;
  }
  * { margin: 0; padding: 0; box-sizing: border-box; }
  html, body {
    width: 1200px;
    height: 843px;
    overflow: hidden;
    background: var(--backdrop);
    font-family: "Open Sans", Arial, sans-serif;
  }
  .stage {
    position: relative;
    width: 1200px;
    height: 843px;
  }
  .card {
    position: absolute;
    left: 290px;
    width: 620px;
    height: 354px;
    box-shadow: 0 6px 18px rgba(0, 0, 0, 0.18);
  }
  /* Back side */
  .card-back {
    top: 40px;
    background: linear-gradient(135deg, var(--navy-light) 0%, var(--navy) 55%, var(--navy-deep) 100%);
    color: var(--paper);
  }
  .card-back .back-name {
    position: absolute;
    left: 0; right: 0;
    top: 148px;
    text-align: center;
    font-size: 40px;
    font-weight: 700;
    letter-spacing: 0.5px;
  }
  .card-back .back-url {
    position: absolute;
    left: 0; right: 0;
    bottom: 26px;
    text-align: center;
    font-size: 14px;
    letter-spacing: 1px;
  }
  /* Front side */
  .card-front {
    top: 449px;
    background: var(--paper);
    color: var(--ink);
  }
  .holder {
    position: absolute;
    left: 44px;
    top: 52px;
  }
  .holder-name {
    font-size: 22px;
    font-weight: 700;
    color: var(--navy);
    line-height: 1.1;
  }
  .holder-title {
    font-size: 14px;
    margin-top: 2px;
  }
  .office {
    font-size: 14.5px;
    line-height: 1.35;
  }
  .holder .office { margin-top: 18px; }
  .contact-line {
    display: flex;
    align-items: center;
    gap: 9px;
  }
  .contact-line svg {
    width: 12px;
    height: 12px;
    fill: var(--navy);
    flex: none;
  }
  .office-secondary {
    position: absolute;
    left: 262px;
    top: 236px;
  }
  .brand {
    position: absolute;
    right: 44px;
    top: 96px;
    display: flex;
    align-items: center;
    gap: 10px;
  }
  .brand-mark {
    width: 16px;
    height: 16px;
    background: var(--navy);
  }
  .brand-name {
    font-size: 36px;
    font-weight: 700;
    color: var(--navy);
    line-height: 1;
  }
</style>
</head>
<body>
<main class="stage">

  <section class="card card-back" aria-label="Business card, back">
    <div class="back-name">BrevoLunt</div>
    <div class="back-url">www.brevolunt.com</div>
  </section>

  <section class="card card-front" aria-label="Business card, front">
    <div class="holder">
      <div class="holder-name">Rowan Ashby</div>
      <div class="holder-title">CEO/Founder</div>
      <div class="office">
        <div>4120 Alder Crest Way</div>
        <div>Fairview, Alaska 34210</div>
        <div class="contact-line">
          <svg viewBox="0 0 24 24" aria-hidden="true"><path d="M6.6 10.8c1.4 2.8 3.8 5.1 6.6 6.6l2.2-2.2c.3-.3.7-.4 1-.2 1.1.4 2.3.6 3.6.6.6 0 1 .4 1 1V20c0 .6-.4 1-1 1C10.6 21 3 13.4 3 4c0-.6.4-1 1-1h3.5c.6 0 1 .4 1 1 0 1.3.2 2.5.6 3.6.1.3 0 .7-.2 1z"/></svg>
          <span>555 218 4076</span>
        </div>
        <div class="contact-line">
          <svg viewBox="0 0 24 24" aria-hidden="true"><path d="M2 5h20v14H2z M3 6l9 7 9-7" stroke="#fff" stroke-width="1.6"/></svg>
          <span>rowan@brevolunt.com</span>
        </div>
        <div class="contact-line">
          <svg viewBox="0 0 24 24" aria-hidden="true"><circle cx="12" cy="12" r="10"/></svg>
          <span>www.brevolunt.com</span>
        </div>
      </div>
    </div>

    <div class="brand">
      <span class="brand-mark" aria-hidden="true"></span>
      <span class="brand-name">BrevoLunt</span>
    </div>

    <div class="office office-secondary">
      <div>4120 Alder Crest Way</div>
      <div>Fairview, Alaska 34210</div>
      <div class="contact-line">
        <svg viewBox="0 0 24 24" aria-hidden="true"><path d="M6.6 10.8c1.4 2.8 3.8 5.1 6.6 6.6l2.2-2.2c.3-.3.7-.4 1-.2 1.1.4 2.3.6 3.6.6.6 0 1 .4 1 1V20c0 .6-.4 1-1 1C10.6 21 3 13.4 3 4c0-.6.4-1 1-1h3.5c.6 0 1 .4 1 1 0 1.3.2 2.5.6 3.6.1.3 0 .7-.2 1z"/></svg>
        <span>555 218 4076</span>
      </div>
    </div>
  </section>

</main>
</body>
</html>
```